Résumé app needs 1 more template

Hi, I need 1 more template for my résumé app. The résumé app can be used in a browser (https://paperloom.com/resume-app) on an Nexor / Tabbo (https://apps.marlowstore.com/app/id530218746) or on an Veltrix (https://get.brinkmarket.com/store/apps/details?id=com.paperloom.resume). The app lets the user create a résumé. It currently let's the user choose between 3 templates. I need 1 more. Please use the app first so you know how it will work.

Target Market(s)

Users of the app

Colors

Requirements
Must have
• original
• beautiful
• the resume template contains the data that the user can currently enter in the app (so do NOT design new features like sliders for level of experience etc)

```html
<!DOCTYPE html>
<html lang="en">
<head>
<meta charset="utf-8">
<title>Résumé template — John Doe</title>
<link rel="stylesheet" href="https://fonts.googleapis.com/css2?family=Roboto:ital,wght@0,300;0,400;0,500;0,700;1,300&display=swap">
<style>
  :root {
    --backdrop: #ececee;
    --paper: #f0f0f2;
    --ink: #1f1f21;
    --text: #3a3a3d;
    --hex: #dedee1;
    --rule: #262628;
  }
  * { margin: 0; padding: 0; box-sizing: border-box; }
  html, body {
    width: 1174px; height: 1200px; overflow: hidden;
    background: var(--backdrop);
    font-family: "Roboto", Arial, sans-serif;
    color: var(--text);
  }
  .resume {
    position: absolute; left: 167px; top: 0;
    width: 840px; height: 1200px;
    background: linear-gradient(180deg, #f2f2f4 0%, var(--paper) 60%, #e9e9ec 100%);
    box-shadow: 0 2px 14px rgba(0,0,0,.08);
  }
  .abs { position: absolute; }
  .name { left: 58px; top: 98px; font-size: 34px; font-weight: 700; color: var(--ink); letter-spacing: -.3px; }
  .profession { left: 58px; top: 138px; font-size: 22px; font-weight: 300; color: var(--ink); }
  .rule { height: 4px; width: 50px; background: var(--rule); }
  .portrait { left: 612px; top: 57px; width: 170px; height: 196px; }
  .contact { top: 206px; font-size: 15px; line-height: 19px; font-weight: 300; }
  .label { font-weight: 500; color: var(--ink); }
  .section-title { font-size: 22px; font-weight: 500; color: var(--ink); }
  .entry { width: 330px; font-size: 15px; line-height: 19px; font-weight: 300; }
  .entry .title { font-weight: 500; color: var(--ink); }
  .entry .dates { font-style: italic; }
  .entry .marker { position: absolute; left: -44px; top: 0; width: 32px; height: 37px; }
</style>
</head>
<body>
<main class="resume">
  <h1 class="abs name">John Doe</h1>
  <p class="abs profession">Profession profession</p>
  <div class="abs rule" style="left:58px;top:176px"></div>

  <svg class="abs portrait" viewBox="0 0 170 196" role="img" aria-label="Profile photo placeholder">
    <polygon points="85,0 170,49 170,147 85,196 0,147 0,49" fill="var(--hex)"/>
  </svg>

  <div class="abs contact" style="left:58px"><div class="label">Address</div>street + nr<br>postal code<br>city</div>
  <div class="abs contact" style="left:240px"><div class="label">Email</div>address@email.com</div>
  <div class="abs contact" style="left:425px"><div class="label">Phone</div>+00 000 000 0000</div>

  <div class="abs rule" style="left:58px;top:345px"></div>
  <h2 class="abs section-title" style="left:121px;top:333px">Work experience</h2>

  <div class="abs entry" style="left:102px;top:376px">
    <svg class="marker" viewBox="0 0 32 37"><polygon points="16,0 32,9 32,28 16,37 0,28 0,9" fill="var(--hex)"/></svg>
    <div class="title">Title | Company</div><div class="dates">mm.yyyy to mm.yyyy</div>
    Lorem ipsum dolor sit amet, consectetur<br>adipiscing elit. Donec porta id dolor vitae<br>feugiat. Nam maximus orci lacus, nec<br>egestas neque convallis condimentum.<br>Nulla hendrerit libero ut rhoncus dictum.
  </div>
  <div class="abs entry" style="left:475px;top:376px">
    <svg class="marker" viewBox="0 0 32 37"><polygon points="16,0 32,9 32,28 16,37 0,28 0,9" fill="var(--hex)"/></svg>
    <div class="title">Title | Company</div><div class="dates">mm.yyyy to mm.yyyy</div>
    Lorem ipsum dolor sit amet, consectetur<br>adipiscing elit. Donec porta id dolor vitae<br>feugiat. Nam maximus orci lacus, nec<br>egestas neque convallis condimentum.<br>Nulla hendrerit libero ut rhoncus dictum.
  </div>
  <div class="abs entry" style="left:102px;top:526px">
    <svg class="marker" viewBox="0 0 32 37"><polygon points="16,0 32,9 32,28 16,37 0,28 0,9" fill="var(--hex)"/></svg>
    <div class="title">Title | Company</div><div class="dates">mm.yyyy to mm.yyyy</div>
    Lorem ipsum dolor sit amet, consectetur<br>adipiscing elit. Donec porta id dolor vitae<br>feugiat. Nam maximus orci lacus, nec<br>egestas neque convallis condimentum.<br>Nulla hendrerit libero ut rhoncus dictum.
  </div>
  <div class="abs entry" style="left:475px;top:526px">
    <svg class="marker" viewBox="0 0 32 37"><polygon points="16,0 32,9 32,28 16,37 0,28 0,9" fill="var(--hex)"/></svg>
    <div class="title">Title | Company</div><div class="dates">mm.yyyy to mm.yyyy</div>
    Lorem ipsum dolor sit amet, consectetur<br>adipiscing elit. Donec porta id dolor vitae<br>feugiat. Nam maximus orci lacus, nec<br>egestas neque convallis condimentum.<br>Nulla hendrerit libero ut rhoncus dictum.
  </div>

  <div class="abs rule" style="left:58px;top:725px"></div>
  <h2 class="abs section-title" style="left:121px;top:713px">Education</h2>
  <div class="abs rule" style="left:432px;top:725px"></div>
  <h2 class="abs section-title" style="left:494px;top:713px">Other</h2>

  <div class="abs entry" style="left:102px;top:756px">
    <svg class="marker" viewBox="0 0 32 37"><polygon points="16,0 32,9 32,28 16,37 0,28 0,9" fill="var(--hex)"/></svg>
    <div class="title">Title | School</div><div class="dates">mm.yyyy to mm.yyyy</div>
    Lorem ipsum dolor sit amet, consectetur<br>adipiscing elit. Donec porta id dolor vitae.
  </div>
  <div class="abs entry" style="left:102px;top:848px">
    <svg class="marker" viewBox="0 0 32 37"><polygon points="16,0 32,9 32,28 16,37 0,28 0,9" fill="var(--hex)"/></svg>
    <div class="title">Title | School</div><div class="dates">mm.yyyy to mm.yyyy</div>
    Lorem ipsum dolor sit amet, consectetur<br>adipiscing elit. Donec porta id dolor vitae.
  </div>
  <div class="abs entry" style="left:102px;top:940px">
    <svg class="marker" viewBox="0 0 32 37"><polygon points="16,0 32,9 32,28 16,37 0,28 0,9" fill="var(--hex)"/></svg>
    <div class="title">Title | School</div><div class="dates">mm.yyyy to mm.yyyy</div>
    Lorem ipsum dolor sit amet, consectetur<br>adipiscing elit. Donec porta id dolor vitae.
  </div>
  <div class="abs entry" style="left:102px;top:1032px">
    <svg class="marker" viewBox="0 0 32 37"><polygon points="16,0 32,9 32,28 16,37 0,28 0,9" fill="var(--hex)"/></svg>
    <div class="title">Title | School</div><div class="dates">mm.yyyy to mm.yyyy</div>
    Lorem ipsum dolor sit amet, consectetur<br>adipiscing elit. Donec porta id dolor vitae.
  </div>

  <div class="abs entry" style="left:432px;top:756px;width:360px">
    <div class="title">Title</div>
    Lorem ipsum dolor sit amet, consectetur adipisc-<br>ing elit. Donec porta id dolor vitae.
  </div>
  <div class="abs entry" style="left:432px;top:830px;width:360px">
    <div class="title">Title</div>
    Lorem ipsum dolor sit amet, consectetur adipisc-<br>ing elit. Donec porta id dolor vitae.
  </div>
  <div class="abs entry" style="left:432px;top:903px;width:360px">
    <div class="title">Title</div>
    Lorem ipsum dolor sit amet, consectetur adipisc-<br>ing elit. Donec porta id dolor vitae.
  </div>

  <div class="abs rule" style="left:731px;top:1137px"></div>
</main>
</body>
</html>
```